International Supplier needs an eye catching profssional letterhead and continuation page

We need a letterhead and continuation sheet designed for a company based in Austria called VULMA Screens GmbH. We develop and install innovate glass partition wall solutions to commercial and cultural buildings and to some of the most contemporary architectural buildings in Europe. I have our inhouse design brief confirming our corporate colours, fonts and images and have our corporate logo available in a variety of formats including AI and EPS. We are open to differing design suggestions as long as they follow the colour and font specification in our corporate design brief. We are at the forefront of innovation, craftmanship and design for architectural glass, framing systems and fire rated partition systems. The final design should communicate the spirit and strength of the company.
www.vulma.com / www.parvoline.co.uk / www.emberpane.com

Target Market(s)

Architects, planners, designers, building contractors and construction companies

Industry/Entity Type

Architecture

Font styles to use
Sans Serif

Requirements
Must have
• VULMA Screens GmbH
• Lindorferweg 14 B
• 4815 Marholden
• Österreich
• Tel: +43 (1) 482 6170
• E-mail:office@vulmascreens.at
• Web:www.vulmascreens.at / www.vulmaemberpane.com
• subtle yet professionally distinctive
• colours and fonts to be taken ffom VULMA design guide but we are also open to variations on the same theme
Should not have
• No bold lines

```html
<!DOCTYPE html>
<html lang="en">
<head>
<meta charset="utf-8">
<title>VULMA Screens GmbH – Letterhead</title>
<link href="https://fonts.googleapis.com/css2?family=Open+Sans:wght@300;400&family=Arimo:wght@700&display=swap" rel="stylesheet">
<style>
  :root {
    --brand-red: #c8103e;
    --ink: #2b2b2b;
    --text: #3a3a3a;
    --paper: #ffffff;
    --backdrop: #e3e4e4;
    --sig-tone: #d9d9d9;
  }
  * { box-sizing: border-box; margin: 0; padding: 0; }
  html, body { width: 1200px; height: 973px; overflow: hidden; }
  body {
    background: var(--backdrop);
    font-family: "Open Sans", sans-serif;
    color: var(--text);
    position: relative;
  }
  .letterhead {
    position: absolute;
    left: 270px; top: 20px;
    width: 660px; height: 933px;
    background: var(--paper);
    box-shadow: 0 2px 10px rgba(0,0,0,.12);
    overflow: hidden;
  }
  .brand {
    position: absolute; left: 56px; top: 46px;
    display: flex; align-items: center; gap: 10px;
  }
  .brand-square { width: 30px; height: 30px; background: var(--brand-red); }
  .brand-name {
    font-weight: 300; font-size: 38px; letter-spacing: 1px;
    color: var(--ink); line-height: 1;
  }
  .letter-body {
    position: absolute; left: 80px; top: 168px; width: 490px;
  }
  .salutation {
    font-family: "Arimo", sans-serif; font-weight: 700;
    font-size: 14px; color: #111; margin-bottom: 16px;
  }
  .letter-body p {
    font-size: 11.4px; line-height: 1.42; margin-bottom: 15px;
  }
  .signature {
    position: absolute; left: 82px; top: 712px;
    width: 140px; height: 52px;
    background: var(--sig-tone); border-radius: 4px;
  }
  .footer-art { position: absolute; left: 0; top: 820px; }
  .contact-line, .address-line, .web-link {
    position: absolute; color: #fff; font-size: 10.5px; line-height: 1;
    white-space: nowrap;
  }
  .contact-line { left: 60px; top: 878px; display: flex; gap: 14px; align-items: center; }
  .contact-line span { display: flex; align-items: center; gap: 5px; }
  .address-line { left: 60px; top: 899px; font-size: 10px; }
  .web-link { right: 26px; font-size: 10px; }
  .web-link.primary { top: 838px; }
  .web-link.secondary { top: 862px; }
</style>
</head>
<body>
  <main class="letterhead">
    <header class="brand">
      <div class="brand-square"></div>
      <div class="brand-name">VULMA</div>
    </header>

    <section class="letter-body">
      <div class="salutation">Dear Mr. Harlan,</div>
      <p>Lorem Ipsum is simply dummy text of the printing and typesetting industry. Lorem Ipsum has been the industry's standard dummy text ever since the 1500s, when an unknown printer took a galley of type and scrambled it to make a type specimen book. It has survived not only five centuries, but also the leap into electronic typesetting, remaining essentially unchanged.</p>
      <p>The standard chunk of Lorem Ipsum used since the 1500s is reproduced below for those interested. Sections 1.10.32 and 1.10.33 from "de Finibus Bonorum et Malorum" by Corvinus are also reproduced in their exact original form, accompanied by English versions from the 1914 translation by H.Marlow.</p>
      <p>Lorem Ipsum is simply dummy text of the printing and typesetting industry. Lorem Ipsum has been the industry's standard dummy text ever since the 1500s, when an unknown printer took a galley of type and scrambled it to make a type specimen book. It has survived not only five centuries, but also the leap into electronic typesetting, remaining essentially unchanged. It was popularised in the</p>
      <p>The standard chunk of Lorem Ipsum used since the 1500s is reproduced below for those interested. Sections 1.10.32 and 1.10.33 from "de Finibus Bonorum et Malorum" by Corvinus are also reproduced in their exact original form, accompanied by English versions from the 1914 translation by H.Marlow</p>
      <p>The standard chunk of Lorem Ipsum used since the 1500s is reproduced below for those interested. Sections 1.10.32 and 1.10.33 from "de Finibus Bonorum et Malorum" by Corvinus are also reproduced in their exact original form.</p>
    </section>

    <div class="signature" role="img" aria-label="Handwritten signature of the sender"></div>

    <footer>
      <svg class="footer-art" width="660" height="113" viewBox="0 0 660 113" aria-hidden="true">
        <rect x="0" y="48" width="478" height="65" fill="var(--brand-red)"/>
        <rect x="0" y="100" width="478" height="1.2" fill="#fff"/>
        <rect x="494" y="6" width="166" height="56" fill="var(--brand-red)"/>
        <rect x="494" y="34" width="166" height="1.2" fill="#fff"/>
        <polygon points="486,30 506,46 486,62 466,46" fill="var(--brand-red)"/>
        <polygon points="486,36 499,46 486,56 473,46" fill="#fff"/>
      </svg>
      <div class="contact-line">
        <span>
          <svg width="10" height="10" viewBox="0 0 10 10"><rect width="10" height="10" rx="1.5" fill="#fff"/><path d="M3 2.2c.5 2.4 2 4 4.6 4.8l.4-1.2-1.5-.6-.6.6c-.8-.4-1.4-1-1.8-1.8l.6-.6L4.1 1.9z" fill="var(--brand-red)"/></svg>
          +43 (1) 482 6170
        </span>
        <span>
          <svg width="11" height="9" viewBox="0 0 11 9"><rect width="11" height="9" rx="1.5" fill="#fff"/><path d="M2 2.5l3.5 2.5L9 2.5" stroke="var(--brand-red)" fill="none" stroke-width="1"/></svg>
          office@vulmascreens.at
        </span>
      </div>
      <div class="address-line">VULMA Screens GmbH, Lindorferweg 14 B, 4815 Marholden Österreich</div>
      <div class="web-link primary">www.vulmascreens.at</div>
      <div class="web-link secondary">www.vulmaemberpane.com</div>
    </footer>
  </main>
</body>
</html>
```